Steadfast MD - Sleep Medicine Specialist - Business Cards

We are a new medical practice called Steadfast MD. We are sleep medicine specialists and we will be conducting sleep studies on patients with sleep related ailments. We want the business card to be bold, professional, and clean with the logo as the stand out visual piece. We dont like wild flashy designs. We want our design to be bold and classic while at the same time conveying who we are and what we do. We are reliable, professional, and the best in the business.

Industry/Entity Type

Health Care

Contact Information for Business Card

- Clean
- Bold
- Classic
- not cluttered

Requirements
Must have
• logo, website, phone number
Nice to have
• several options to choose from
Should not have
• flashy imaged - reflective print - images of people sleeping

```html
<!DOCTYPE html>
<html lang="en">
<head>
<meta charset="utf-8">
<title>Steadfast MD – Business Card</title>
<link rel="stylesheet" href="https://fonts.googleapis.com/css2?family=Roboto:wght@300;400;500;700;900&display=swap">
<style>
  :root {
    --brand-red: #e81e25;
    --ink: #111111;
    --card-white: #fafafa;
    --band-black: #0d0d0d;
    --backdrop: #2a2a2a;
  }
  * { margin: 0; padding: 0; box-sizing: border-box; }
  html, body { width: 1200px; height: 969px; overflow: hidden; }
  body {
    background: var(--backdrop);
    font-family: "Roboto", Arial, sans-serif;
    position: relative;
  }
  .card {
    position: absolute;
    left: 295px;
    width: 615px;
    height: 352px;
    border-radius: 21px;
    overflow: hidden;
  }
  .card--front { top: 90px; background: var(--card-white); }
  .card--back { top: 529px; background: var(--brand-red); }

  .wordmark {
    position: absolute;
    left: 25px;
    top: 42px;
    font-weight: 700;
    font-size: 35px;
    letter-spacing: -1px;
    color: var(--ink);
    line-height: 1;
  }
  .person { position: absolute; left: 26px; top: 118px; }
  .person__name {
    font-weight: 700;
    font-size: 21px;
    color: var(--ink);
    line-height: 1.1;
  }
  .person__name .accent { color: var(--brand-red); }
  .person__role { font-size: 14px; color: var(--ink); margin-top: 1px; }

  .address {
    position: absolute;
    left: 26px;
    top: 174px;
    font-weight: 300;
    font-size: 14.5px;
    line-height: 18px;
    color: var(--ink);
  }
  .contacts {
    position: absolute;
    left: 25px;
    top: 226px;
    list-style: none;
  }
  .contacts li {
    display: flex;
    align-items: center;
    height: 20.5px;
    font-weight: 300;
    font-size: 14.5px;
    color: var(--ink);
  }
  .contacts svg { width: 12px; height: 12px; margin-right: 8px; flex: none; }

  .emblem-ring {
    position: absolute;
    left: 351px;
    top: 61px;
    width: 230px;
    height: 230px;
  }
  .bottom-band { position: absolute; left: 0; bottom: 0; width: 615px; height: 22px; }

  .back-lockup {
    position: absolute;
    left: 0; right: 0;
    top: 0; bottom: 0;
    display: flex;
    align-items: center;
    justify-content: center;
    gap: 10px;
  }
  .back-lockup__ring { width: 102px; height: 102px; }
  .back-lockup__name {
    font-weight: 700;
    font-size: 48px;
    letter-spacing: -1.5px;
    color: #ffffff;
    line-height: 1;
  }
</style>
</head>
<body>
  <section class="card card--front" aria-label="Business card front">
    <div class="wordmark">Steadfast MD</div>

    <div class="person">
      <div class="person__name">DANIEL <span class="accent">HARPER</span></div>
      <div class="person__role">Manager</div>
    </div>

    <div class="address">
      512 N. Lake Ave.<br>
      Country name , MN 41873
    </div>

    <ul class="contacts">
      <li>
        <svg viewBox="0 0 12 12" aria-hidden="true"><path fill="#e81e25" d="M2.6 1c.4 0 .7.2.8.5l.8 1.7c.1.3 0 .6-.2.8l-.7.6c.4 1 1.2 1.8 2.2 2.2l.6-.7c.2-.2.5-.3.8-.2l1.7.8c.3.1.5.4.5.8v1.2c0 .6-.5 1-1.1 1C4.6 9.5 1.5 6.4 1.3 2.1c0-.6.4-1.1 1-1.1z"/></svg>
        (555) 4170 - 2236
      </li>
      <li>
        <svg viewBox="0 0 12 12" aria-hidden="true"><rect x="3" y="0.7" width="6" height="10.6" rx="1" fill="none" stroke="#e81e25" stroke-width="1"/><circle cx="6" cy="9.6" r="0.6" fill="#e81e25"/></svg>
        (555) 3804 - 6612
      </li>
      <li>
        <svg viewBox="0 0 12 12" aria-hidden="true"><rect x="0.5" y="2.5" width="11" height="7" fill="#e81e25"/><path d="M0.8 2.8 6 6.8l5.2-4" fill="none" stroke="#fafafa" stroke-width="0.9"/></svg>
        info@steadfastmd.com
      </li>
      <li>
        <svg viewBox="0 0 12 12" aria-hidden="true"><circle cx="6" cy="6" r="5.3" fill="none" stroke="#e81e25" stroke-width="1"/><ellipse cx="6" cy="6" rx="2.3" ry="5.3" fill="none" stroke="#e81e25" stroke-width="0.8"/><path d="M0.8 6h10.4" stroke="#e81e25" stroke-width="0.8"/></svg>
        www.steadfastmdclinic.com
      </li>
    </ul>

    <svg class="emblem-ring" viewBox="0 0 230 230" aria-hidden="true">
      <circle cx="115" cy="115" r="111" fill="none" stroke="#e81e25" stroke-width="8"/>
    </svg>

    <svg class="bottom-band" viewBox="0 0 615 22" preserveAspectRatio="none" aria-hidden="true">
      <polygon points="0,0 317,0 303,22 0,22" fill="#e81e25"/>
      <polygon points="323,0 615,0 615,22 309,22" fill="#0d0d0d"/>
    </svg>
  </section>

  <section class="card card--back" aria-label="Business card back">
    <div class="back-lockup">
      <svg class="back-lockup__ring" viewBox="0 0 102 102" aria-hidden="true">
        <circle cx="51" cy="51" r="48" fill="none" stroke="#ffffff" stroke-width="4"/>
      </svg>
      <span class="back-lockup__name">Steadfast MD</span>
    </div>
  </section>
</body>
</html>
```